Heron Ridge Distillery Bottle Label Design

We need a label design for a product called "Coldwater Mill Straight Bourbon Whiskey". The bottle has two embossments on the side and an image printed on the back that will show through when looking from the front (shown in the attached image). It's made of 30% rye and 70% corn; images of the ingredients can be incorporated into the label design. We are a distillery that produces whiskey and bourbon from local farmers around the area. We focus on the quality of the ingredients and using the recipes passed down from generation to generation. We like a straight forward design using two colors maximum. The background will be brown once filled with the bourbon, so it must contrast against it (i.e. white and other lighter colors). The Heron Ridge Distillery logo must be present on the bottle front, as well as 750 ml, 84 PROOF, 42% ALC/VOL.

Target Market(s)

Craft whiskey consumers.

Industry/Entity Type

Product

Colors
fee18a
fbe7d2
fff3d1
fefcee
fefdec
fdf9cf

Requirements
Must have
• 750 ml, 84 PROOF, 42% ALC/VOL. Aged for 3 years.The Heron Ridge Distillery logo must be present on the bottle. Only two colors on label.
Nice to have
• Story of how we are a micro distillery making hand crafted whiskey.
Should not have
• False or misleading print.

```html
<!DOCTYPE html>
<html lang="en">
<head>
<meta charset="utf-8">
<title>Heron Ridge Distillery – Coldwater Mill Straight Bourbon Whiskey Label</title>
<link rel="stylesheet" href="https://fonts.googleapis.com/css2?family=Oswald:wght@400;500;600&display=swap">
<style>
  :root {
    --bourbon-deep: #6a2a08;
    --bourbon-mid: #9a4510;
    --bourbon-light: #c0661c;
    --label-gold: #fee18a;
    --label-cream: #fff3d1;
    --label-white: #fefcee;
    --rule: rgba(254, 225, 138, 0.85);
  }
  * { box-sizing: border-box; margin: 0; padding: 0; }
  html, body {
    width: 1200px;
    height: 1000px;
    overflow: hidden;
  }
  body {
    background: radial-gradient(ellipse at 50% 40%, var(--bourbon-light) 0%, var(--bourbon-mid) 45%, var(--bourbon-deep) 100%);
    font-family: "Oswald", "Arial Narrow", sans-serif;
  }
  .label {
    position: absolute;
    left: 50%;
    top: 0;
    width: 520px;
    height: 1000px;
    transform: translateX(-50%);
    display: flex;
    flex-direction: column;
    align-items: center;
  }
  .brand-mark {
    margin-top: 58px;
    width: 88px;
    height: 88px;
    border-radius: 50%;
    background: var(--label-gold);
  }
  .brand-name {
    margin-top: 14px;
    color: var(--label-gold);
    font-weight: 600;
    font-size: 62px;
    line-height: 1;
    letter-spacing: 1px;
  }
  .brand-sub {
    margin-top: 8px;
    padding: 4px 0;
    width: 330px;
    text-align: center;
    color: var(--label-gold);
    font-weight: 600;
    font-size: 28px;
    letter-spacing: 10px;
    line-height: 1.1;
    border-top: 2px solid var(--rule);
    border-bottom: 2px solid var(--rule);
    text-indent: 10px;
  }
  .age-ribbon {
    margin-top: 30px;
    position: relative;
    width: 300px;
    height: 42px;
  }
  .age-ribbon svg { position: absolute; inset: 0; }
  .age-ribbon span {
    position: relative;
    display: block;
    text-align: center;
    line-height: 42px;
    color: var(--bourbon-deep);
    font-weight: 500;
    font-size: 22px;
    letter-spacing: 1px;
  }
  .ornament {
    width: 300px;
    height: 16px;
    border-radius: 8px;
    background: linear-gradient(90deg, transparent, rgba(254,225,138,0.55), transparent);
  }
  .ornament--top { margin-top: 20px; }
  .ornament--bottom { margin-top: 14px; }
  .product-place {
    margin-top: 10px;
    color: var(--label-gold);
    font-weight: 500;
    font-size: 44px;
    letter-spacing: 5px;
    line-height: 1;
  }
  .product-grade {
    margin-top: 10px;
    background: var(--label-gold);
    color: var(--bourbon-mid);
    font-weight: 500;
    font-size: 46px;
    letter-spacing: 5px;
    line-height: 1;
    padding: 6px 14px 8px 19px;
  }
  .product-type {
    margin-top: 10px;
    color: var(--label-white);
    font-weight: 500;
    font-size: 100px;
    line-height: 0.98;
    text-align: center;
    letter-spacing: 1px;
  }
  .farm-scene {
    margin-top: 14px;
    width: 520px;
    height: 128px;
    border-radius: 4px;
    background: linear-gradient(180deg, rgba(254,225,138,0.05) 0%, rgba(251,231,210,0.25) 60%, rgba(254,225,138,0.4) 100%);
  }
  .spec-line {
    margin-top: 22px;
    display: flex;
    border-top: 2px solid var(--rule);
    border-bottom: 2px solid var(--rule);
    color: var(--label-gold);
    font-weight: 500;
    font-size: 22px;
    letter-spacing: 1px;
    line-height: 1;
  }
  .spec-line span { padding: 6px 12px; }
  .spec-line span + span { border-left: 2px solid var(--rule); }
</style>
</head>
<body>
  <main class="label">
    <div class="brand-mark" aria-hidden="true"></div>
    <div class="brand-name">Heron Ridge</div>
    <div class="brand-sub">DISTILLERY</div>

    <div class="age-ribbon">
      <svg viewBox="0 0 300 42" width="300" height="42" aria-hidden="true">
        <polygon points="0,4 300,4 286,21 300,38 0,38 14,21" fill="#fee18a"/>
        <rect x="22" y="9" width="256" height="24" fill="none" stroke="#9a4510" stroke-width="1.5"/>
      </svg>
      <span>AGED FOR 3 YEARS</span>
    </div>

    <div class="ornament ornament--top" role="img" aria-label="Decorative scroll flourish"></div>

    <div class="product-place">COLDWATER MILL</div>
    <div class="product-grade">STRAIGHT</div>
    <h1 class="product-type">BOURBON<br>WHISKEY</h1>

    <div class="ornament ornament--bottom" role="img" aria-label="Decorative scroll flourish"></div>

    <div class="farm-scene" role="img" aria-label="Crossed wheat stalks over a faded farm scene with barn and grain silos"></div>

    <div class="spec-line">
      <span>84 PROOF</span>
      <span>42%ALC/VOL</span>
      <span>750ml</span>
    </div>
  </main>
</body>
</html>
```